Business card for Chiropractic clinics needs reworked / redesigned

The business card in attachment was designed 10 years ago. It is in need of an update.
We have 2 clinics:
HALSPUNT VORDA & HALSPUNT MIRBE
Only one address needs to be on the card for doctors that only work in one clinic and two addresses need to be on the card for the doctors that work in both clinics.

Target Market(s)

patients/referrers

Industry/Entity Type

Medical

Contact Information for Business Card

Logo (in full or zoomed-in)
Clinic Name
Doctor name and title
clinic address, website, tel, email

Font styles to use
Sans Serif

Colors

Designer to choose colors to be used in the design.

Requirements
Must have
• Good contrast/readability
• We like modern minimalistic designs
• The Bcard needs to project our very high standard of proficiency/professionalism
Should not have
• Not curly
• Not to much colours

```html
<!DOCTYPE html>
<html lang="en">
<head>
<meta charset="utf-8">
<title>Halspunt Vorda – Business Card</title>
<link href="https://fonts.googleapis.com/css2?family=Lato:wght@400;700&display=swap" rel="stylesheet">
<style>
  :root {
    --stage: #3b322e;
    --card-white: #ffffff;
    --card-black: #0b0b0c;
    --ink: #17262b;
    --ink-soft: #2f3b40;
    --rule: #c9c9c9;
    --on-dark: #f2f2f2;
  }
  * { box-sizing: border-box; margin: 0; padding: 0; }
  html, body { width: 1200px; height: 844px; overflow: hidden; }
  body {
    background: var(--stage);
    font-family: 'Lato', sans-serif;
    position: relative;
  }
  .card {
    position: absolute;
    top: 248px;
    width: 540px;
    height: 348px;
    border-radius: 4px;
  }
  .card--front { left: 45px; background: var(--card-white); color: var(--ink); }
  .card--back {
    left: 615px;
    background: linear-gradient(160deg, #1d1d1f 0%, var(--card-black) 70%);
    color: var(--on-dark);
  }
  .brand-mark {
    position: absolute;
    display: flex;
    align-items: center;
    gap: 8px;
    font-weight: 700;
    letter-spacing: 0.06em;
  }
  .brand-mark__square { width: 12px; height: 12px; background: currentColor; }
  .card--front .brand-mark { right: 40px; top: 52px; font-size: 15px; color: var(--ink); }
  .rule {
    position: absolute;
    right: 34px;
    height: 1px;
    background: var(--rule);
  }
  .rule--a { top: 108px; width: 290px; }
  .rule--b { top: 140px; width: 430px; }
  .rule--c { top: 228px; width: 470px; }
  .rule--d { top: 284px; width: 480px; }
  .person { position: absolute; left: 34px; top: 170px; }
  .person__name { font-size: 22px; font-weight: 700; letter-spacing: 0.01em; line-height: 1.05; }
  .person__title { font-size: 17px; font-weight: 400; color: var(--ink-soft); letter-spacing: 0.02em; }
  .clinic { position: absolute; left: 34px; top: 240px; font-size: 15px; line-height: 1.3; }
  .clinic__name { font-weight: 700; }
  .contact { position: absolute; left: 34px; top: 296px; font-size: 15px; }
  .contact b { font-weight: 700; }
  .card--back .brand-mark {
    left: 0; right: 0; top: 140px;
    justify-content: center;
    font-size: 20px;
  }
  .website {
    position: absolute;
    left: 0; right: 0; top: 250px;
    text-align: center;
    font-size: 15px;
    letter-spacing: 0.02em;
  }
</style>
</head>
<body>
  <section class="card card--front" aria-label="Business card front">
    <div class="brand-mark"><span class="brand-mark__square"></span>HALSPUNT VORDA</div>
    <div class="rule rule--a"></div>
    <div class="rule rule--b"></div>
    <div class="person">
      <p class="person__name">JORIS VERHAEGHE</p>
      <p class="person__title">CHIROPRACTOR</p>
    </div>
    <div class="rule rule--c"></div>
    <div class="clinic">
      <p class="clinic__name">HALSPUNT VORDA</p>
      <p class="clinic__address">Beukenlaan 48&nbsp; 9000 Vorda</p>
    </div>
    <div class="rule rule--d"></div>
    <p class="contact"><b>P:</b> +32 (0)9 000.14.52&nbsp; | <b>E:</b> info@halspuntvorda.be</p>
  </section>

  <section class="card card--back" aria-label="Business card back">
    <div class="brand-mark"><span class="brand-mark__square"></span>HALSPUNT VORDA</div>
    <p class="website">www.halspuntvorda.be</p>
  </section>
</body>
</html>
```